Flyer-Design für Kindertagesstätte
Helmsteds Kinderhafen suchte ein neues Design in der Kategorie Flyer und hat ein Projekt auf grafikfinden.de gestartet.
Zielgruppe
Wir sind eine Kindertagesstätte und wollen eine Baby-Kind-Spielgruppe jeden Mittwoch in unserer Kita von 09.00 Uhr bis 11.00 Uhr anbieten.
Aufgabenstellung
Unser LOGO muss im Flyer enthalten sein, auf jeden Fall ein Bild wenn möglich mit mehreren Babys/Kleinkindern bis 1,5 Jahre. Wir benötigen den Flyer in DIN lang - bunt - 1 seitig.
Folgender Text sollte enthalten: Baby-Kind-Spielgruppe, jeden mittwoch in unserer Kita 'Helmsteds Kinderhafen' von 09.00 Uhr bis 11.00 Uhr. Die Spielgruppe wird durch unser ausgebildetes Fachpersonal begleitet.

```html
<!DOCTYPE html>
<html lang="de">
<head>
<meta charset="utf-8">
<title>Baby-Kind-Spielgruppe – Helmsteds Kinderhafen</title>
<link rel="stylesheet" href="https://fonts.googleapis.com/css2?family=Open+Sans:wght@400;600;700;800&display=swap">
<style>
  :root {
    --page-bg: #e6e6e6;
    --paper: #ffffff;
    --brand-brown: #5e1a14;
    --teal: #1b9b9a;
    --magenta: #b02282;
    --orange: #e0822a;
    --blue: #1a93d4;
    --ink: #1a1a1a;
    --white: #ffffff;
  }
  * { box-sizing: border-box; margin: 0; padding: 0; }
  html, body { width: 1200px; height: 800px; overflow: hidden; }
  body {
    background: var(--page-bg);
    font-family: "Open Sans", Arial, sans-serif;
    display: flex; align-items: center; justify-content: center;
  }
  .flyer {
    position: relative;
    width: 352px; height: 740px;
    background: var(--paper);
    box-shadow: 0 2px 10px rgba(0,0,0,0.12);
    overflow: hidden;
  }
  .brand {
    position: absolute; top: 38px; left: 0; right: 0;
    display: flex; align-items: center; justify-content: center; gap: 10px;
  }
  .brand__mark {
    width: 14px; height: 14px; border-radius: 50%;
    background: var(--brand-brown);
  }
  .brand__name {
    color: var(--brand-brown);
    font-weight: 600; font-size: 23px; letter-spacing: 0.3px;
  }
  .headline {
    position: absolute; top: 118px; left: 28px; right: 0; height: 118px;
    background: var(--teal); color: var(--white);
    display: flex; flex-direction: column; justify-content: center;
    text-align: center; padding: 0 12px;
  }
  .headline__title { font-weight: 800; font-size: 25px; letter-spacing: 0.4px; line-height: 1.15; }
  .headline__info { font-weight: 600; font-size: 12.5px; line-height: 1.35; margin-top: 6px; }
  .photo {
    position: absolute; top: 246px; left: 28px; right: 0; height: 224px;
    background: linear-gradient(135deg, #f4e2b8 0%, #f0c94a 35%, #e9b9b0 65%, #9ec37a 100%);
  }
  .note {
    position: absolute; color: var(--white); font-weight: 600;
    font-size: 13.5px; line-height: 1.35; text-align: center;
    display: flex; align-items: center; justify-content: center; padding: 0 14px;
  }
  .note--staff { top: 470px; left: 28px; width: 206px; height: 92px; background: var(--magenta); }
  .note--signup { top: 562px; left: 50px; width: 206px; height: 86px; background: var(--orange); }
  .mascot {
    position: absolute; top: 486px; left: 256px; width: 78px; height: 84px;
    border-radius: 40px 40px 18px 18px;
    background: linear-gradient(180deg, #d89a4a 0%, #6b2a1c 100%);
  }
  .mascot-brand {
    position: absolute; top: 578px; left: 238px; width: 112px;
    text-align: center; color: var(--brand-brown);
    font-weight: 600; font-size: 13px; line-height: 1.2;
  }
  .contact {
    position: absolute; top: 648px; left: 60px; right: 0; height: 56px;
    background: var(--blue); color: var(--white);
    display: flex; align-items: center; justify-content: center; gap: 10px;
  }
  .contact__icon { width: 24px; height: 24px; }
  .contact__phone { font-weight: 800; font-size: 26px; letter-spacing: 0.5px; }
  .website {
    position: absolute; top: 712px; left: 60px; right: 0;
    text-align: center; color: var(--ink);
    font-weight: 800; font-size: 13px;
  }
</style>
</head>
<body>
  <main class="flyer">
    <header class="brand">
      <span class="brand__mark"></span>
      <span class="brand__name">Helmsteds Kinderhafen</span>
    </header>

    <section class="headline">
      <h1 class="headline__title">BABY-KIND-SPIELGRUPPE</h1>
      <p class="headline__info">jeden mittwoch in unserer Kita<br>'Helmsteds Kinderhafen' von 09.00 Uhr bis 11.00 Uhr</p>
    </section>

    <div class="photo" role="img" aria-label="Foto: zwei Kleinkinder spielen auf dem Boden einer Kita mit bunten Stapelringen und einem Spielzeuglaster"></div>

    <p class="note note--staff">Die Spielgruppe wird durch unser ausgebildetes Fachpersonal begleitet</p>
    <p class="note note--signup">Voranmeldungen bitte unter telefonisch und website unter :</p>

    <div class="mascot" role="img" aria-label="Illustration: Maskottchen der Kita"></div>
    <p class="mascot-brand">Helmsteds Kinderhafen</p>

    <section class="contact">
      <svg class="contact__icon" viewBox="0 0 24 24" aria-hidden="true">
        <path fill="#ffffff" d="M6.6 10.8a15 15 0 0 0 6.6 6.6l2.2-2.2a1 1 0 0 1 1-.25 11.4 11.4 0 0 0 3.6.57 1 1 0 0 1 1 1V20a1 1 0 0 1-1 1A17 17 0 0 1 3 4a1 1 0 0 1 1-1h3.5a1 1 0 0 1 1 1c0 1.25.2 2.45.57 3.57a1 1 0 0 1-.25 1z"/>
      </svg>
      <span class="contact__phone">0351-7284160</span>
    </section>
    <p class="website">www.helmsteds-kinderhafen.de</p>
  </main>
</body>
</html>
```